Modern & Fresh Sumeray Book Cover

Need a creative e-book cover for my book.

Title: Get Sumeray Sorted
Subtitle: Learn How To Easily Choose & Enroll in the Perfect Coverage at the Perfect Time.

Target Market(s)

60-70 year olds in the United States

Font styles to use
Sans Serif

Colors
9bcb3c
33a6d7

Requirements
Must have
• Must look modern and fresh.
• Use our company colors www.BrovaMint.com

```html
<!DOCTYPE html>
<html lang="en">
<head>
<meta charset="utf-8">
<title>Get Sumeray Sorted – BrovaMint</title>
<link rel="stylesheet" href="https://fonts.googleapis.com/css2?family=Open+Sans:wght@400;700;800&display=swap">
<style>
  :root {
    --lime: #9df03a;
    --lime-deep: #8fdc34;
    --sky: #4ccef2;
    --white: #ffffff;
  }
  html, body {
    margin: 0;
    padding: 0;
    overflow: hidden;
    background: #ffffff;
  }
  .cover {
    position: relative;
    width: 849px;
    height: 1200px;
    overflow: hidden;
    font-family: "Open Sans", Arial, sans-serif;
    color: var(--white);
  }
  .cover-art {
    position: absolute;
    inset: 0;
  }
  .brand {
    position: absolute;
    top: 48px;
    right: 80px;
    text-align: center;
  }
  .brand-mark {
    display: block;
    width: 26px;
    height: 26px;
    margin: 0 auto 6px;
    border-radius: 50%;
    background: var(--white);
  }
  .brand-name {
    font-weight: 800;
    font-size: 64px;
    line-height: 1;
    letter-spacing: -0.5px;
  }
  .brand-tagline {
    margin-top: 4px;
    font-weight: 700;
    font-size: 7.5px;
    letter-spacing: 1.2px;
    text-transform: uppercase;
    text-align: right;
  }
  /* Axis runs along the long diagonal rule, starting where the rule begins */
  .title-axis {
    position: absolute;
    left: 85px;
    top: 268px;
    width: 0;
    height: 0;
    transform-origin: 0 0;
    transform: rotate(45deg);
  }
  .title {
    position: absolute;
    left: 97px;
    bottom: 2px;
    margin: 0;
    font-weight: 800;
    font-size: 74px;
    line-height: 1;
    letter-spacing: -1px;
    text-transform: uppercase;
    white-space: nowrap;
  }
  .subtitle {
    position: absolute;
    left: 87px;
    top: 8px;
    margin: 0;
    font-weight: 400;
    font-size: 23px;
    line-height: 1.2;
    white-space: nowrap;
  }
  .contact {
    position: absolute;
    left: 26px;
    bottom: 64px;
    list-style: none;
    margin: 0;
    padding: 0;
  }
  .contact li {
    display: flex;
    align-items: center;
    height: 32px;
    margin-top: 28px;
  }
  .contact-dot {
    width: 30px;
    height: 30px;
    border-radius: 50%;
    background: var(--white);
  }
  .contact-web {
    margin-left: 26px;
    font-weight: 700;
    font-size: 23px;
  }
</style>
</head>
<body>
  <main class="cover">
    <svg class="cover-art" width="849" height="1200" viewBox="0 0 849 1200">
      <defs>
        <radialGradient id="photo-tint" cx="45%" cy="50%" r="70%">
          <stop offset="0" stop-color="var(--lime)"/>
          <stop offset="1" stop-color="var(--lime-deep)"/>
        </radialGradient>
      </defs>
      <rect width="849" height="1200" fill="url(#photo-tint)" role="img" aria-label="Faint lime-tinted photo of a senior couple reviewing paperwork together"/>
      <polygon points="292,0 849,0 849,406 613,456" fill="var(--sky)"/>
      <polygon points="0,755 214,740 556,1200 0,1200" fill="var(--sky)"/>
      <g stroke="var(--white)" stroke-width="3" fill="none">
        <line x1="57" y1="395" x2="271" y2="142"/>
        <line x1="107" y1="335" x2="221" y2="228"/>
        <line x1="85" y1="268" x2="781" y2="964"/>
      </g>
    </svg>

    <header class="brand">
      <span class="brand-mark"></span>
      <div class="brand-name">BrovaMint</div>
      <div class="brand-tagline">Sumeray educational workshops</div>
    </header>

    <section class="title-axis">
      <h1 class="title">Get Sumeray Sorted</h1>
      <p class="subtitle">Learn How To Easily Choose &amp; Enroll in the Perfect Coverage at the Perfect Time</p>
    </section>

    <ul class="contact">
      <li><span class="contact-dot"></span></li>
      <li><span class="contact-dot"></span></li>
      <li><span class="contact-dot"></span><span class="contact-web">www.BrovaMint.com</span></li>
    </ul>
  </main>
</body>
</html>
```